Invitation to Retail Shopping Event

-Must include logo
-Can contain product pictures depending on design
-I prefer any graphics to be my own product pictures
-Should include the following language:
Sip and Shop
Thursday, November 18
11 to 1 pm
487 Birch Lane
Come enjoy sips, snacks and shopping! Be the first to preview our new winter collection and get an early start on your holiday gifting.
Please RSVP to 415-382-9061 or info@brivettenw.com

```html
<!DOCTYPE html>
<html lang="en">
<head>
<meta charset="utf-8">
<title>Brivette Sip &amp; Shop Invitation</title>
<link rel="stylesheet" href="https://fonts.googleapis.com/css2?family=Italianno&family=Josefin+Sans:wght@400;600&family=Montserrat:wght@400&display=swap">
<style>
  :root {
    --page-bg: #ececec;
    --gold-edge: #d4ae5a;
    --gold-light: #f8f29e;
    --navy: #272b35;
    --copper-line: #b8732f;
    --cocoa: #7a4535;
    --pill: #a26b52;
    --pill-text: #f3e3cf;
    --white: #ffffff;
  }
  * { margin: 0; padding: 0; box-sizing: border-box; }
  html, body { width: 1200px; height: 1200px; overflow: hidden; background: var(--page-bg); }
  .invitation {
    position: absolute; left: 186px; top: 0; width: 828px; height: 1200px;
    background: linear-gradient(to bottom, var(--gold-edge) 0%, var(--gold-light) 47%, var(--gold-edge) 100%);
    font-family: "Josefin Sans", sans-serif; color: var(--cocoa);
  }
  .side-band { position: absolute; top: 0; height: 1200px; width: 66px; background: var(--navy); }
  .side-band--left { left: 24px; }
  .side-band--right { left: 737px; }
  .side-rule { position: absolute; top: 0; height: 1200px; width: 2px; background: var(--copper-line); }
  .side-rule--left { left: 43px; }
  .side-rule--right { left: 783px; }

  .centered { position: absolute; left: 414px; transform: translateX(-50%); white-space: nowrap; text-align: center; }

  .brand-name { top: 94px; font-size: 44px; font-weight: 600; letter-spacing: 3px; color: var(--white); }

  .event-title { top: 196px; font-family: "Italianno", cursive; font-size: 132px; line-height: 1; color: var(--cocoa); }

  .date-row { position: absolute; top: 0; left: 0; width: 828px; }
  .date-month { position: absolute; left: 250px; top: 380px; font-size: 22px; }
  .date-year { position: absolute; left: 530px; top: 380px; font-size: 22px; }
  .date-weekday { top: 362px; left: 427px; font-size: 22px; }
  .date-day { top: 388px; left: 427px; font-size: 36px; }
  .date-divider { position: absolute; top: 378px; width: 2px; height: 36px; background: var(--cocoa); }
  .date-divider--left { left: 363px; }
  .date-divider--right { left: 502px; }

  .time-pill {
    position: absolute; left: 320px; top: 462px; width: 188px; height: 45px;
    background: var(--pill); border-radius: 22px 8px 22px 8px;
    font-family: "Montserrat", sans-serif; font-size: 25px; letter-spacing: 3px;
    color: var(--pill-text); text-align: center; line-height: 47px;
  }

  .venue { top: 556px; font-size: 27px; }
  .tagline { top: 628px; font-size: 30px; line-height: 39px; }
  .divider { position: absolute; left: 294px; top: 729px; }
  .details { top: 788px; font-size: 23px; line-height: 30px; }
  .rsvp { top: 894px; font-size: 24px; line-height: 32px; }
  .rsvp-phone { top: 924px; font-size: 26px; }
  .rsvp-or { top: 962px; font-size: 22px; }
  .rsvp-email { top: 1008px; font-size: 24px; }

  .product-photo {
    position: absolute; top: 920px; width: 124px; height: 120px; border-radius: 50%;
    background: radial-gradient(circle, #c9962e 0%, #b8842a 45%, rgba(212,174,90,0) 72%);
  }
  .product-photo--left { left: 126px; }
  .product-photo--right { left: 570px; }

  .footer-rule { position: absolute; top: 1115px; height: 2px; background: var(--cocoa); }
  .footer-rule--left { left: 206px; width: 62px; }
  .footer-rule--right { left: 562px; width: 60px; }
  .footer-ornament {
    position: absolute; left: 268px; top: 1102px; width: 294px; height: 28px;
    background: linear-gradient(to right, rgba(122,69,53,0.35), rgba(122,69,53,0.6), rgba(122,69,53,0.35));
    border-radius: 14px;
  }
</style>
</head>
<body>
  <main class="invitation">
    <div class="side-band side-band--left"></div>
    <div class="side-rule side-rule--left"></div>
    <div class="side-band side-band--right"></div>
    <div class="side-rule side-rule--right"></div>

    <div class="centered brand-name">BRIVETTE</div>

    <h1 class="centered event-title">Sip &amp; Shop</h1>

    <div class="date-row">
      <span class="date-month">November</span>
      <span class="date-divider date-divider--left"></span>
      <span class="centered date-weekday">Thursday</span>
      <span class="centered date-day">18</span>
      <span class="date-divider date-divider--right"></span>
      <span class="date-year">2021</span>
    </div>

    <div class="time-pill">11 to 1 pm</div>

    <p class="centered venue">487 Birch Lane</p>

    <p class="centered tagline">Come enjoy sips,<br>snacks and shopping !</p>

    <svg class="divider" width="240" height="14" viewBox="0 0 240 14" aria-hidden="true">
      <path d="M0 7 Q60 5 112 3 L112 11 Q60 9 0 7 Z" fill="#7a4535"/>
      <path d="M240 7 Q180 5 128 3 L128 11 Q180 9 240 7 Z" fill="#7a4535"/>
      <circle cx="104" cy="7" r="3.5" fill="#7a4535"/>
      <path d="M120 3 L124 7 L120 11 L116 7 Z" fill="#7a4535"/>
      <circle cx="136" cy="7" r="3.5" fill="#7a4535"/>
    </svg>

    <p class="centered details">Be the first to preview our new winter collection<br>and get an early start on your holiday gifting.</p>

    <p class="centered rsvp">Please RSVP to</p>
    <p class="centered rsvp-phone">415-382-9061</p>
    <p class="centered rsvp-or">or</p>
    <p class="centered rsvp-email">info@brivettenw.com</p>

    <div class="product-photo product-photo--left" role="img" aria-label="Photo of a gold quatrefoil ring set with small stones"></div>
    <div class="product-photo product-photo--right" role="img" aria-label="Photo of a gold quatrefoil ring set with small stones"></div>

    <div class="footer-rule footer-rule--left"></div>
    <div class="footer-ornament" role="img" aria-label="Decorative scroll flourish"></div>
    <div class="footer-rule footer-rule--right"></div>
  </main>
</body>
</html>
```